Business Card Design for Kind Helper

I am starting my own consultancy business, using what I learned in marketing and advertising to help Non -profits with marketing and communications needs. I need a professional business card design to hand out to my clients.

My business name is “Outreach2Kindness” my vision is that this need this to be reflective of marketing doing good for the world through the power of communications. I like the color palettes in olives, creams and oranges but am open to design options.
In addition to the cards I am asking for separate file for the logo and will need a JPG, PSD Vector File.

Information to go on the card:

Morwenna Calloway
Marketing Consultant
Email: outreach2kindness@mailbrook.com, callowaym1@brinmoreu.edu
Website: Outreach2Kindness.com

Communications

```html
<!DOCTYPE html>
<html lang="en">
<head>
<meta charset="utf-8">
<title>Outreach2Kindness – Business Card</title>
<link rel="stylesheet" href="https://fonts.googleapis.com/css2?family=Arimo:wght@400;700&family=Michroma&display=swap">
<style>
  :root {
    --brand-blue: #1a69b4;
    --accent-red: #c8213d;
    --card-white: #ffffff;
    --bg-light: #8d8d8d;
    --bg-dark: #4f4f4f;
    --ink-light: #ffffff;
  }
  * { margin: 0; padding: 0; box-sizing: border-box; }
  html, body { width: 1200px; height: 1000px; overflow: hidden; }
  body {
    position: relative;
    background: linear-gradient(135deg, var(--bg-light) 0%, #878787 55%, var(--bg-dark) 100%);
    font-family: "Arimo", Arial, sans-serif;
  }
  .card {
    position: absolute;
    box-shadow: 0 1px 3px rgba(0,0,0,0.45);
  }
  .card--front {
    left: 37px; top: 48px; width: 542px; height: 315px;
    background: var(--brand-blue);
    color: var(--ink-light);
  }
  .card--back {
    left: 614px; top: 48px; width: 544px; height: 318px;
    background: var(--card-white);
  }
  .brand {
    position: absolute;
    left: 0; right: 0;
    display: flex; align-items: center; justify-content: center;
    gap: 14px;
  }
  .brand__name {
    font-family: "Arimo", Arial, sans-serif;
    font-weight: 400;
    letter-spacing: 0.5px;
  }
  .card--front .brand { top: 88px; }
  .card--front .brand__name { font-size: 34px; color: var(--ink-light); }
  .card--back .brand { top: 120px; }
  .card--back .brand__name { font-size: 36px; color: var(--brand-blue); }

  .person {
    position: absolute;
    right: 307px; top: 228px;
    text-align: right;
  }
  .person__name {
    font-family: "Michroma", "Arial", sans-serif;
    font-size: 18.5px;
    line-height: 26px;
    white-space: nowrap;
  }
  .person__role {
    font-size: 15px;
    line-height: 22px;
    margin-top: 2px;
  }
  .divider {
    position: absolute;
    left: 245px; top: 222px;
    width: 1.5px; height: 62px;
    background: var(--ink-light);
  }
  .contacts {
    position: absolute;
    left: 254px; top: 220px;
    list-style: none;
    font-size: 15px;
  }
  .contacts li {
    display: flex; align-items: center;
    height: 21px;
    white-space: nowrap;
  }
  .contacts svg { width: 13px; height: 13px; margin-right: 7px; flex: none; }
</style>
</head>
<body>

  <section class="card card--front" aria-label="Business card front">
    <div class="brand">
      <svg width="48" height="48" viewBox="0 0 48 48" aria-hidden="true">
        <circle cx="24" cy="24" r="20" fill="none" stroke="var(--ink-light)" stroke-width="5"/>
      </svg>
      <span class="brand__name">Outreach2Kindness</span>
    </div>

    <div class="person">
      <p class="person__name">Morwenna Calloway</p>
      <p class="person__role">Marketing Consultant</p>
    </div>

    <div class="divider"></div>

    <ul class="contacts">
      <li>
        <svg viewBox="0 0 13 13" aria-hidden="true"><rect x="3" y="0.5" width="7" height="12" rx="1.2" fill="#fff"/><rect x="4.3" y="2" width="4.4" height="4" fill="var(--brand-blue)"/></svg>
        555.204.7781
      </li>
      <li>
        <svg viewBox="0 0 13 13" aria-hidden="true"><rect x="0.5" y="2.5" width="12" height="8" fill="#fff"/><path d="M0.5 2.5 L6.5 7 L12.5 2.5" fill="none" stroke="var(--brand-blue)" stroke-width="1"/></svg>
        outreach2kindness@mailbrook.com
      </li>
      <li>
        <svg viewBox="0 0 13 13" aria-hidden="true"><circle cx="6.5" cy="6.5" r="5.6" fill="none" stroke="#fff" stroke-width="1.3"/><ellipse cx="6.5" cy="6.5" rx="2.4" ry="5.6" fill="none" stroke="#fff" stroke-width="1"/><line x1="1" y1="6.5" x2="12" y2="6.5" stroke="#fff" stroke-width="1"/></svg>
        Outreach2Kindness.com
      </li>
    </ul>
  </section>

  <section class="card card--back" aria-label="Business card back">
    <div class="brand">
      <svg width="56" height="56" viewBox="0 0 56 56" aria-hidden="true">
        <circle cx="28" cy="28" r="24" fill="var(--brand-blue)" stroke="var(--accent-red)" stroke-width="6"/>
      </svg>
      <span class="brand__name">Outreach2Kindness</span>
    </div>
  </section>

</body>
</html>
```